Salt Under Canvas: Years of Quiet Marching

I am an independent author writing a book about my life in the military while serving under the Don't Ask, Don't Tell Policy. The book will be published in both print and E-book format. For the print book, the front cover should be military dog tags with the main title printed on the tags while the subtitle printed at the top. The bottom portion of the front cover should have my name, "Bernard L. Whitfield". For the spine, the main title and my name should appear. The back will be reserved for the book's teaser as well as web contact information, both of which I will provide at a later time (still in development). The E-book cover can simply be the same as the front cover design for the print book.
Updates

Update! Change of heart on the positioning of the main title and the subtitle. Prefer the main title above the subtitle.

Thanks for all the submissions thus far.  Lots to choose from!  I finally have some info for the back covers.  If you have time, could you include the following on the back.

An unapologetic, first-hand account of life under Don’t Ask, Don’t Tell (make sure this is in big bold print at top)

(This is the teaser to be placed under) From 1993 to 2011, the Don’t Ask, Don’t Tell Policy affected the way LGBT military personnel not only interacted with people in public, but among each other in private.  From using code words in public to engaging in a secret sex life in private, the policy created a ridiculous social construct under which LGBT military personnel were expected to adhere.  For six and a half years, the author lived under these rules with the help of love-interests, friends, and allied co-workers.  Salt Under Canvas recalls episodes of the author living life to the fullest while covering his tracks just enough to avoid getting caught.  Despite enduring injustice, the author demonstrates just how resilient the LGBT community actually was.  Whether it was secret gatherings, a disciplined code of silence, or simply looking out for each other, Salt Under Canvas seeks to tell the story few have a guts to admit: how LGBT personnel got around the rules of Don’t Ask, Don’t Tell in order to maintain some sense of dignity

(The following contact info is to be placed toward the bottom centered.  Leave enough space to still place an ISBN)

www.facebook.com/saltcanvasbook           www.salt-canvas.com              www.twitter.com/saltcanvasbook

Hi Designers!

Lots of wonderful submissions that I appreciate very much.  Just an FYI, I intend to publish the print book cover via Print Harbor.  The instructions for book covers is found via the following link:

The design that I go with will need to adhere to these specifications.  No worries if your does not comply with these parameters at the time being.  I have every intention of offering payment for additional revisions to the covers.  Please send me quotes for additional revisions once the contest is over.  Also, to the design I pick, I will also require an E-book avatar, but we can discuss this later.

Target Market(s)

Target audience for this book are LGBT 25 and older, and women 25 and older

Requirements
Must have
• Dog Tags with main title printed on it.
Nice to have
• Print book and the E-book are going to have the same design, so try to ensure that the front cover design can catch attention as a thumbnail on a webpage.

```html
<!DOCTYPE html>
<html lang="en">
<head>
<meta charset="utf-8">
<title>Salt Under Canvas — Book Cover</title>
<link href="https://fonts.googleapis.com/css2?family=Caprasimo&family=Arvo:wght@700&display=swap" rel="stylesheet">
<style>
  :root{
    --stage:#e8e8e8;
    --cover-light:#f2f2f2;
    --cover-mid:#c9c9c9;
    --cover-dark:#8e8e8e;
    --ink:#1a1a1a;
    --box:#0d0d0d;
    --box-text:#f4f4f4;
    --tag-light:#d8d8d8;
    --tag-dark:#3a3a3a;
    --spine:#bdbdbd;
  }
  *{box-sizing:border-box;margin:0;padding:0}
  html,body{width:1200px;height:800px;overflow:hidden;background:var(--stage)}
  .canvas{position:relative;width:1200px;height:800px}
  .cover-spread{position:absolute;left:200px;top:110px;display:flex;height:580px}

  .back-cover{
    width:380px;height:580px;position:relative;overflow:hidden;
    background:radial-gradient(ellipse at 50% 45%,var(--cover-light) 0%,var(--cover-mid) 60%,var(--cover-dark) 100%);
    padding:26px 28px;
  }
  .back-author{font-family:'Arvo',serif;font-weight:700;font-size:9px;text-align:right;color:var(--ink);padding-right:40px}
  .back-title{font-family:'Caprasimo',serif;font-weight:400;font-size:25px;color:var(--ink);line-height:1.1;margin-top:6px;white-space:nowrap;text-align:center}
  .back-rule{border:0;border-top:2px solid var(--ink);margin:6px 0 8px}
  .back-subtitle{font-family:'Arvo',serif;font-weight:700;font-size:10.5px;text-align:center;color:var(--ink);letter-spacing:.3px}
  .back-teaser{
    font-family:'Arvo',serif;font-weight:700;font-size:8px;line-height:1.5;color:var(--ink);
    text-transform:uppercase;text-align:justify;text-align-last:center;margin-top:26px;
  }
  .back-boxes{position:absolute;left:28px;right:28px;bottom:30px;display:flex;justify-content:space-between}
  .back-box{width:116px;height:56px;background:var(--box);color:var(--box-text);
    font-family:'Arvo',serif;font-weight:700;font-size:12px;display:flex;align-items:center;justify-content:center}

  .spine{
    width:38px;height:580px;overflow:hidden;
    background:linear-gradient(90deg,var(--cover-dark),var(--spine) 40%,var(--cover-mid));
    display:flex;align-items:flex-start;justify-content:center;padding-top:16px;
  }
  .spine-text{writing-mode:vertical-rl;font-family:'Caprasimo',serif;font-size:20px;color:var(--ink);white-space:nowrap;display:flex;gap:70px;align-items:center}
  .spine-author{font-family:'Arvo',serif;font-weight:700;font-size:9px}

  .front-cover{
    width:380px;height:580px;position:relative;overflow:hidden;
    background:radial-gradient(ellipse at 55% 40%,var(--cover-light) 0%,#dcdcdc 55%,var(--cover-mid) 100%);
  }
  .dog-tags-photo{
    position:absolute;left:26px;top:40px;width:340px;height:420px;border-radius:40px;
    background:radial-gradient(ellipse at 60% 45%,var(--tag-light) 0%,#a9a9a9 55%,var(--tag-dark) 100%);
    opacity:.85;
  }
  .tag-title,.tag-subtitle{position:absolute;color:var(--ink);text-align:center}
  .tag-title{left:90px;top:90px;width:240px;font-family:'Caprasimo',serif;font-weight:400;font-size:30px;line-height:1.1}
  .tag-subtitle{left:100px;top:280px;width:220px;font-family:'Caprasimo',serif;font-weight:400;font-size:17px;line-height:1.2}
  .front-author{position:absolute;left:0;right:0;bottom:40px;text-align:center;font-family:'Arvo',serif;font-weight:700;font-size:13px;color:var(--ink)}
</style>
</head>
<body>
<main class="canvas">
  <div class="cover-spread">
    <section class="back-cover">
      <p class="back-author">BERNARD L. WHITFIELD</p>
      <h2 class="back-title">SALT UNDER CANVAS</h2>
      <hr class="back-rule">
      <p class="back-subtitle">YEARS OF QUIET MARCHING</p>
      <p class="back-teaser">
        Lorem ipsum dolor sit amet, consectetur adipisicing elit, sed do eiusmod tempor incididunt ut labore et dolore magna aliqua. Ut enim ad minim veniam, quis nostrud exercitation.
        Lorem ipsum dolor sit amet, consectetur adipisicing elit, sed do eiusmod tempor incididunt ut labore et dolore magna aliqua. Ut enim ad minim veniam, quis nostrud exercitation.
        Lorem ipsum dolor sit amet, consectetur adipisicing elit, sed do eiusmod tempor incididunt ut labore et dolore magna aliqua. Ut enim ad minim veniam, quis nostrud exercitation.
        Lorem ipsum dolor sit amet, consectetur adipisicing elit, sed do eiusmod tempor incididunt ut labore et dolore magna aliqua. Ut enim ad minim veniam, quis nostrud exercitation.
        Lorem ipsum dolor sit amet, consectetur adipisicing elit, sed do eiusmod tempor incididunt ut labore et dolore magna aliqua. Ut enim ad minim veniam, quis nostrud exercitation.
        Lorem ipsum dolor sit amet, consectetur adipisicing elit, sed do eiusmod tempor incididunt ut labore et dolore magna aliqua. Ut enim ad minim veniam.
      </p>
      <div class="back-boxes">
        <div class="back-box">LOGO</div>
        <div class="back-box">ISBN</div>
      </div>
    </section>

    <section class="spine">
      <p class="spine-text"><span>SALT UNDER CANVAS</span><span class="spine-author">BERNARD L. WHITFIELD</span></p>
    </section>

    <section class="front-cover">
      <div class="dog-tags-photo" role="img" aria-label="Photograph of two military dog tags with rubber silencers hanging on a ball chain"></div>
      <h1 class="tag-title">SALT UNDER<br>CANVAS</h1>
      <p class="tag-subtitle">YEARS<br>OF QUIET<br>MARCHING</p>
      <p class="front-author">BERNARD L. WHITFIELD</p>
    </section>
  </div>
</main>
</body>
</html>
```